my website is toncielbrode.com. (brand name is ton ciel brodé) This is just a template that i have choose for. The content and the pictures are not about my business just the template.
I would like to have 4 pages for now. 1 homepage, which will be an overview for all pages, it is right now in this way. It will directly highlight my story. My website will tell an exclusive story about details which makes the difference and will make people happy with very small things. It will be art related but very stylish as well. I also want to have a event agenda on my homepage where people can see where my next event is. Page 2 my blog, where I will write weekly about mindset, lifestyle and details. Inspiration place for people who are looking for unique and exclusive approaches in life. Page 3 shop, where I will sell my stuff which is handmade and unique, it will be limited edition stuff. Mostly I will make the designs from marbling art, which I am a teacher for. (https://www.vidorama-example.com/watch?v=Xk3pQr7LmZa) check this video out for more. Page 4 is book page. Here people will be able to book private or group classes for marbling art (check the video). I have already a community of more than 500 people on join nest, which will be my public as well. I wanna implement the join nest button on this page as well. to be able to track.

This is about my website. I also need a logo for my brand, which will suit my website and my goals.

I can also give you a reference website, which really like as structure and style;
https://www.brightmorrowgoods-example.com/products/the-quiet-ledger?gclid=Zx8RtYpWq2LmN4vBcD6sKjH3gFaE9uIoP1lKzXcVbNm7QwErTyUiOp0AsDfGhJkLzXcVbNm5Qw2ErTyUi_oPaSd8FgHjKlZxC_vbNQ

ton ciel brodé

4 page

• I can also give you a reference website, which really like as structure and style;
• https://www.brightmorrowgoods-example.com/products/the-quiet-ledger?gclid=Zx8RtYpWq2LmN4vBcD6sKjH3gFaE9uIoP1lKzXcVbNm7QwErTyUiOp0AsDfGhJkLzXcVbNm5Qw2ErTyUi_oPaSd8FgHjKlZxC_vbNQ

```html
<!DOCTYPE html>
<html lang="en">
<head>
<meta charset="utf-8">
<title>ton ciel brodé — online store</title>
<link rel="stylesheet" href="https://fonts.googleapis.com/css2?family=Open+Sans:wght@400;600;700&display=swap">
<style>
:root{
  --ink:#222;
  --muted:#555;
  --white:#fff;
  --line:#d9d9d9;
  --brown-dark:#4a200a;
  --brown:#6b3414;
  --brown-light:#8a4a1f;
  --events-dark:#161a14;
  --events-mid:#262c22;
  --star:#b48a2a;
  --badge:#111;
  --highlight:#dcdcdc;
}
*{box-sizing:border-box;margin:0;padding:0}
html,body{width:1200px;height:2927px;overflow:hidden}
body{font-family:"Open Sans",Arial,sans-serif;color:var(--ink);background:var(--white);position:relative}
a{color:inherit;text-decoration:none}

/* Header */
.site-header{position:absolute;left:0;top:0;width:1200px;height:84px;background:var(--white);z-index:3}
.brand{position:absolute;left:107px;top:22px;display:flex;align-items:center;gap:12px;font-size:26px;font-weight:400;color:var(--ink);letter-spacing:.5px}
.brand-mark{width:14px;height:14px;border-radius:50%;background:var(--ink)}
.utility{position:absolute;right:100px;top:18px;display:flex;gap:18px;font-size:13px;font-weight:600;color:#333;align-items:center}
.utility .sep{color:#999;font-weight:400}
.utility svg{width:13px;height:13px;vertical-align:-2px;margin-right:6px;fill:#555}
.main-nav{position:absolute;left:704px;top:47px;display:flex;gap:20px;font-size:13px;font-weight:600;color:#222}
.main-nav .active{border-bottom:1px solid #222}
.search-box{position:absolute;left:958px;top:43px;width:140px;height:27px;border:1px solid var(--line);font-size:12px;font-weight:600;display:flex;align-items:center;padding-left:12px;gap:28px}
.search-box svg{width:12px;height:12px}

/* Hero */
.hero{position:absolute;left:0;top:84px;width:1200px;height:527px;
  clip-path:polygon(0 0,100% 0,100% 89%,48% 100%,0 89.6%);
  background:linear-gradient(100deg,#3a2b2a 0%,#b9617a 14%,#e9d8d0 26%,#6b4a3a 38%,#d9c9b8 50%,#3e3e55 62%,#c7b7a8 74%,#7d6b9a 86%,#3b2b30 100%)}
.hero-veil{position:absolute;inset:0;background:rgba(20,15,15,.35)}
.hero-title{position:absolute;left:0;width:1200px;top:274px;text-align:center;color:var(--white);font-size:46px;font-weight:700;letter-spacing:1px}
.hero-sub{position:absolute;left:0;width:1200px;top:348px;text-align:center;color:var(--white);font-size:18px;font-weight:600;line-height:21px}
.hero-btn{position:absolute;left:517px;top:427px;width:166px;height:37px;background:#111;color:var(--white);font-size:16px;font-weight:600;display:flex;align-items:center;justify-content:center}
.hero-dots{position:absolute;left:568px;top:548px;display:flex;gap:4px}
.hero-dots span{width:10px;height:10px;border-radius:50%;border:1.5px solid var(--white)}
.hero-dots span.on{background:var(--white)}

/* Section headings */
.section-title{position:absolute;left:0;width:1200px;text-align:center;font-size:25px;font-weight:700;letter-spacing:1px}
.arrow{position:absolute;width:14px;height:20px}
.arrow path{fill:none;stroke:#555;stroke-width:2}

/* Our products */
.product{position:absolute;top:751px;width:189px;text-align:center}
.product-photo{width:189px;height:170px;border:1px solid #ddd;position:relative}
.quick-view{position:absolute;left:50px;top:76px;background:rgba(255,255,255,.9);font-size:12px;font-weight:700;padding:4px 10px}
.product-name{font-size:14px;color:#333;margin-top:9px}
.product-price{font-size:13px;font-weight:700;margin-top:3px}
.add-link{font-size:13px;font-weight:700;display:flex;align-items:center;justify-content:center;gap:8px;margin-top:3px}
.add-link svg{width:13px;height:12px}

/* About */
.about{position:absolute;left:0;top:1044px;width:1200px;height:410px;
  background:radial-gradient(circle at 20% 30%,var(--brown-light) 0,transparent 40%),radial-gradient(circle at 70% 70%,var(--brown-light) 0,transparent 45%),linear-gradient(135deg,var(--brown-dark),var(--brown) 50%,var(--brown-dark));color:var(--white)}
.about h2{position:absolute;left:101px;top:81px;font-size:25px;font-weight:700;letter-spacing:.5px}
.about h3{position:absolute;left:101px;top:126px;font-size:19px;font-weight:700}
.about-copy{position:absolute;left:101px;top:162px;width:480px;font-size:12.5px;line-height:23px}
.about-btn{position:absolute;left:101px;top:310px;width:114px;height:32px;border:1.5px solid var(--white);font-size:14px;font-weight:600;display:flex;align-items:center;justify-content:center}
.about-photo{position:absolute;left:679px;top:86px;width:416px;height:259px;border:8px solid #3a3a3a;background:linear-gradient(120deg,#8a5a18,#6a8a3a 40%,#9ab46a 60%,#7a4a14)}

/* Featured */
.feature{position:absolute;top:1584px;width:178px;height:294px}
.feature.is-hover{background:var(--highlight)}
.feature-photo{width:170px;height:168px;position:relative}
.badge{position:absolute;left:8px;top:6px;background:var(--badge);color:var(--white);font-size:12px;font-weight:600;padding:2px 8px}
.feature-name{font-size:17px;font-weight:600;margin:7px 0 0 6px}
.feature-price{font-size:14px;margin:3px 0 0 6px}
.feature-price s{color:#777;margin-right:6px}
.feature-price b{font-weight:700}
.stars{font-size:13px;color:var(--star);margin:2px 0 0 6px;letter-spacing:1px}
.stars .off{color:#bbb}
.cart-btn{position:absolute;left:6px;top:260px;width:152px;height:33px;border:1.5px solid #bbb;background:var(--white);font-size:15px;font-weight:700;display:flex;align-items:center;justify-content:center;gap:12px}
.cart-btn svg{width:15px;height:14px}
.is-hover .cart-btn{background:#111;border-color:#111;color:var(--white)}
.is-hover .cart-btn path{fill:var(--white)}

/* Events */
.events{position:absolute;left:0;top:1959px;width:1200px;height:626px;background:linear-gradient(180deg,var(--events-mid),var(--events-dark));color:var(--white)}
.events .section-title{top:70px;color:var(--white)}
.event{position:absolute;top:127px;width:322px}
.event-photo{width:322px;height:171px;border:3px solid #e8e8e8}
.event h4{font-size:17px;font-weight:700;margin-top:84px}
.event-meta{font-size:12.5px;margin-top:14px;display:flex;gap:14px;align-items:center}
.event-meta svg{width:12px;height:12px;margin-right:5px;vertical-align:-1px}
.event p{font-size:12.5px;line-height:21px;margin-top:12px;width:318px}
.event .more{display:block;font-size:11.5px;font-weight:700;margin-top:12px}

/* Footer */
.site-footer{position:absolute;left:0;top:2585px;width:1200px;height:342px;background:var(--white)}
.foot-col{position:absolute;top:68px}
.foot-col h5{font-size:15px;font-weight:700;margin-bottom:14px}
.foot-about p{width:290px;font-size:12px;line-height:24px;color:var(--muted)}
.contact-line{font-size:12px;color:var(--muted);line-height:24px;display:flex;gap:12px}
.contact-line svg{width:11px;height:11px;margin-top:6px;fill:#777;flex:none}
.socials{display:flex;gap:10px}
.socials span{width:27px;height:27px;border-radius:50%;border:1.5px solid #333;display:flex;align-items:center;justify-content:center}
.socials span i{width:9px;height:9px;background:#333;border-radius:2px}
.field{position:absolute;border:1px solid #bbb;font-size:11px;color:#777;padding:4px 6px}
.send{position:absolute;left:0;top:184px;width:62px;height:24px;background:#000;color:var(--white);font-size:11px;font-weight:700;display:flex;align-items:center;justify-content:center}
.to-top{position:absolute;left:1144px;top:192px;width:28px;height:28px;border-radius:50%;background:#ccc;display:flex;align-items:center;justify-content:center}
.footer-rule{position:absolute;left:100px;top:287px;width:1000px;height:1px;background:#e3e3e3}
.copyright{position:absolute;left:0;width:1200px;top:306px;text-align:center;font-size:12px;color:var(--muted)}
</style>
</head>
<body>

<header class="site-header">
  <a class="brand" href="#"><span class="brand-mark"></span>ton ciel brodé</a>
  <div class="utility">
    <span><svg viewBox="0 0 16 16"><path d="M8 14 2 8a3.5 3.5 0 0 1 6-4 3.5 3.5 0 0 1 6 4z"/></svg>Wishlist(0)</span>
    <span class="sep">|</span>
    <span><svg viewBox="0 0 16 16"><path d="M4 7V5a4 4 0 0 1 8 0v2h1v8H3V7zm2 0h4V5a2 2 0 0 0-4 0z"/></svg>Login / Register</span>
    <span class="sep">|</span>
    <span><svg viewBox="0 0 16 16"><path d="M1 2h3l2 8h8l2-6H5"/><circle cx="7" cy="13" r="1.5"/><circle cx="13" cy="13" r="1.5"/></svg>0 Items</span>
  </div>
  <nav class="main-nav">
    <a class="active" href="#">HOME</a><a href="#">BLOG</a><a href="#">SHOP</a><a href="#">BOOK NOW</a>
  </nav>
  <div class="search-box">
    <svg viewBox="0 0 12 12"><circle cx="5" cy="5" r="3.5" fill="none" stroke="#222" stroke-width="1.6"/><path d="m7.5 7.5 3 3" stroke="#222" stroke-width="1.6"/></svg>
    SEARCH
  </div>
</header>

<section class="hero" role="img" aria-label="Photo of hand-marbled greeting cards displayed on a table">
  <div class="hero-veil"></div>
  <h1 class="hero-title">TRENDSETTING ONLINE STORE</h1>
  <p class="hero-sub">Our first-rate products and exceptional customer service to shoppers<br>from the comfort of their own homes</p>
  <a class="hero-btn" href="#">READ MORE</a>
  <div class="hero-dots"><span class="on"></span><span></span><span></span><span></span></div>
</section>

<h2 class="section-title" style="top:680px">OUR PRODUCTS</h2>
<svg class="arrow" style="left:73px;top:823px" viewBox="0 0 14 20"><path d="M11 2 3 10l8 8"/></svg>
<svg class="arrow" style="left:1110px;top:823px" viewBox="0 0 14 20"><path d="m3 2 8 8-8 8"/></svg>

<div class="product" style="left:101px">
  <div class="product-photo" role="img" aria-label="Marbled paper in purple and cream cells" style="background:linear-gradient(135deg,#7a3a5a,#c89ab8 50%,#5a2a3a)"><span class="quick-view">QUICK VIEW</span></div>
  <div class="product-name">Lorem Ipsum</div>
  <div class="add-link"><svg viewBox="0 0 13 12"><path d="M0 1h2l2 7h7l2-5H3" fill="none" stroke="#111" stroke-width="1.6"/><circle cx="5" cy="10.5" r="1.2"/><circle cx="10" cy="10.5" r="1.2"/></svg>ADD TO CART</div>
</div>
<div class="product" style="left:302px">
  <div class="product-photo" role="img" aria-label="Marbled paper with green and pink floral swirls" style="background:linear-gradient(135deg,#6a9a3a,#e8b0c8 50%,#4a7a5a)"></div>
  <div class="product-name">Lorem Ipsum</div>
  <div class="product-price">$69.00</div>
</div>
<div class="product" style="left:503px">
  <div class="product-photo" role="img" aria-label="Dark marbled paper with pale swirl" style="background:linear-gradient(135deg,#1a1a1a,#3a3a30 50%,#222)"></div>
  <div class="product-name">Lorem Ipsum</div>
  <div class="product-price">$69.00</div>
</div>
<div class="product" style="left:706px">
  <div class="product-photo" role="img" aria-label="Rose and brown marbled paper" style="background:linear-gradient(135deg,#8a4a4a,#d8a8a0 50%,#6a3a3a)"></div>
  <div class="product-name">Lorem Ipsum</div>
  <div class="product-price">$69.00</div>
</div>
<div class="product" style="left:909px">
  <div class="product-photo" role="img" aria-label="Brown and white combed marbled paper" style="background:linear-gradient(135deg,#7a4a2a,#e8e0d8 50%,#5a3a2a)"></div>
  <div class="product-name">Lorem Ipsum</div>
  <div class="product-price">$69.00</div>
</div>

<section class="about">
  <h2>ABOUT US</h2>
  <h3>100 % PERFECT. IT'S ALL ABOUT DETAIL!</h3>
  <p class="about-copy">We provide an unparalleled selection of the very best quality products, an easy and comfortable shopping experience, expedited shipping offers, and exceptional cus tomer service. Check out our collection of new arrivals, best-sellers, and clearance items today.<br>We're a business made up of innovators and forward-thinkers, with the drive and wherewithal to constantly update and improve the online shopping experience.</p>
  <a class="about-btn" href="#">READ MORE</a>
  <div class="about-photo" role="img" aria-label="Hand drawing a marbling pattern with green drops on an amber bath"></div>
</section>

<h2 class="section-title" style="top:1522px">FEATURED PRODUCTS</h2>
<svg class="arrow" style="left:68px;top:1714px" viewBox="0 0 14 20"><path d="M11 2 3 10l8 8"/></svg>
<svg class="arrow" style="left:1112px;top:1714px" viewBox="0 0 14 20"><path d="m3 2 8 8-8 8"/></svg>

<div class="feature" style="left:101px">
  <div class="feature-photo" role="img" aria-label="Oval gold frame with red marbled insert" style="background:linear-gradient(135deg,#c8bca8,#c84a3a 50%,#b8ac98)"><span class="badge">- 40%</span></div>
  <div class="feature-name">Lorem ipsum</div>
  <div class="feature-price"><s>$ 150</s><b>$ 110</b></div>
  <div class="stars">★★★★<span class="off">★</span></div>
  <a class="cart-btn" href="#"><svg viewBox="0 0 15 14"><path d="M0 1h2.5l2 8h8l2-6H4" fill="none" stroke="#111" stroke-width="1.8"/><circle cx="6" cy="12" r="1.4"/><circle cx="11.5" cy="12" r="1.4"/></svg>ADD TO CART</a>
</div>
<div class="feature" style="left:298px">
  <div class="feature-photo" role="img" aria-label="Oval gold frame with marbled cat picture" style="background:linear-gradient(135deg,#e8ddd0,#a8a0a0 50%,#e0d4c4)"></div>
  <div class="feature-name">Lorem ipsum</div>
  <div class="feature-price"><s>$ 150</s><b>$ 120</b></div>
  <div class="stars">★★★★<span class="off">★</span></div>
  <a class="cart-btn" href="#"><svg viewBox="0 0 15 14"><path d="M0 1h2.5l2 8h8l2-6H4" fill="none" stroke="#111" stroke-width="1.8"/><circle cx="6" cy="12" r="1.4"/><circle cx="11.5" cy="12" r="1.4"/></svg>ADD TO CART</a>
</div>
<div class="feature" style="left:509px">
  <div class="feature-photo" role="img" aria-label="Marbled shoe decoration on a dark background" style="background:linear-gradient(135deg,#1a1a22,#d89aa8 50%,#2a2a30)"><span class="badge">- 30%</span></div>
  <div class="feature-name">Lorem ipsum</div>
  <div class="feature-price"><s>$ 150</s><b>$ 110</b></div>
  <div class="stars">★★★★<span class="off">★</span></div>
  <a class="cart-btn" href="#"><svg viewBox="0 0 15 14"><path d="M0 1h2.5l2 8h8l2-6H4" fill="none" stroke="#111" stroke-width="1.8"/><circle cx="6" cy="12" r="1.4"/><circle cx="11.5" cy="12" r="1.4"/></svg>ADD TO CART</a>
</div>
<div class="feature is-hover" style="left:717px">
  <div class="feature-photo" role="img" aria-label="Green marbled paper with a heart-shaped motif" style="background:linear-gradient(135deg,#3a6a2a,#8a4a9a 50%,#2a5a3a)"><span class="badge">- 15%</span></div>
  <div class="feature-name">Lorem ipsum</div>
  <div class="feature-price"><s>$ 180</s><b>$ 150</b></div>
  <div class="stars">★★★★<span class="off">★</span></div>
  <a class="cart-btn" href="#"><svg viewBox="0 0 15 14"><path d="M0 1h2.5l2 8h8l2-6H4" fill="none" stroke="#fff" stroke-width="1.8"/><circle cx="6" cy="12" r="1.4" fill="#fff"/><circle cx="11.5" cy="12" r="1.4" fill="#fff"/></svg>ADD TO CART</a>
</div>
<div class="feature" style="left:927px">
  <div class="feature-photo" role="img" aria-label="Marbled bird motif on a magenta ground" style="background:linear-gradient(135deg,#b82a6a,#e89ab0 50%,#a8225a)"></div>
  <div class="feature-name">Lorem ipsum</div>
  <div class="feature-price"><s>$ 250</s><b>$ 150</b></div>
  <div class="stars">★★★★<span class="off">★</span></div>
  <a class="cart-btn" href="#"><svg viewBox="0 0 15 14"><path d="M0 1h2.5l2 8h8l2-6H4" fill="none" stroke="#111" stroke-width="1.8"/><circle cx="6" cy="12" r="1.4"/><circle cx="11.5" cy="12" r="1.4"/></svg>ADD TO CART</a>
</div>

<section class="events">
  <h2 class="section-title">UPCOMING EVENTS</h2>
  <article class="event" style="left:100px">
    <div class="event-photo" role="img" aria-label="Workshop participants gathered around a marbling table" style="background:linear-gradient(135deg,#6a5a4a,#b8a890 50%,#4a4a52)"></div>
    <h4>PERFECT WAY TO REDUCE STRESS!</h4>
    <div class="event-meta"><span><svg viewBox="0 0 12 12"><rect x="1" y="2" width="10" height="9" fill="none" stroke="#fff" stroke-width="1.4"/><path d="M1 5h10" stroke="#fff"/></svg>OCTOBER 4, 2017</span><span><svg viewBox="0 0 12 12"><circle cx="6" cy="6" r="5" fill="none" stroke="#fff" stroke-width="1.4"/><path d="M6 3v3l2 1" stroke="#fff" fill="none"/></svg>SAT 14:00</span></div>
    <p>Lorem Ipsum is simply dummy text of the printing . It is tLorem Ipsum has been the industry's standard dummy text ever since the 1500s.</p>
    <a class="more" href="#">READ MORE</a>
  </article>
  <article class="event" style="left:435px">
    <div class="event-photo" role="img" aria-label="Two hosts standing behind a table of marbled cards" style="background:linear-gradient(135deg,#d8d0c8,#7a3a3a 50%,#e0d8d0)"></div>
    <h4>WORKSHOP MARBLING</h4>
    <div class="event-meta"><span><svg viewBox="0 0 12 12"><rect x="1" y="2" width="10" height="9" fill="none" stroke="#fff" stroke-width="1.4"/><path d="M1 5h10" stroke="#fff"/></svg>OCTOBER 4, 2017</span><span><svg viewBox="0 0 12 12"><circle cx="6" cy="6" r="5" fill="none" stroke="#fff" stroke-width="1.4"/><path d="M6 3v3l2 1" stroke="#fff" fill="none"/></svg>SAT 14:00</span></div>
    <p>Lorem Ipsum is simply dummy text of the printing . It is tLorem Ipsum has been the industry's standard dummy text ever since the 1500s.</p>
    <a class="more" href="#">READ MORE</a>
  </article>
  <article class="event" style="left:780px">
    <div class="event-photo" role="img" aria-label="Red marbling bath with paint colours on a table" style="background:linear-gradient(180deg,#3a3a34 0,#3a3a34 35%,#c82a22 55%,#8a1a14 80%,#2a2a26)"></div>
    <h4>LOREM IPSUM IS SIMPLE</h4>
    <div class="event-meta"><span><svg viewBox="0 0 12 12"><rect x="1" y="2" width="10" height="9" fill="none" stroke="#fff" stroke-width="1.4"/><path d="M1 5h10" stroke="#fff"/></svg>OCTOBER 4, 2017</span><span><svg viewBox="0 0 12 12"><circle cx="6" cy="6" r="5" fill="none" stroke="#fff" stroke-width="1.4"/><path d="M6 3v3l2 1" stroke="#fff" fill="none"/></svg>SAT 14:00</span></div>
    <p>Lorem Ipsum is simply dummy text of the printing . It is tLorem Ipsum has been the industry's standard dummy text ever since the 1500s.</p>
    <a class="more" href="#">READ MORE</a>
  </article>
</section>

<footer class="site-footer">
  <div class="foot-col foot-about" style="left:100px">
    <h5>ABOUT</h5>
    <p>We're a business made up of innovators and forward-thinkers, with the drive and wherewithal to constantly update and improve the online shopping experience.</p>
  </div>
  <div class="foot-col" style="left:447px">
    <h5>CONTACT</h5>
    <div class="contact-line"><svg viewBox="0 0 12 12"><path d="M6 0a4 4 0 0 0-4 4c0 3 4 8 4 8s4-5 4-8a4 4 0 0 0-4-4zm0 5.5A1.5 1.5 0 1 1 6 2.5a1.5 1.5 0 0 1 0 3z"/></svg><span>ton ciel brodé<br>Linden Row, Kilmore</span></div>
    <div class="contact-line"><svg viewBox="0 0 12 12"><path d="M2 0h2l1 3-1.5 1a7 7 0 0 0 4.5 4.5L9 7l3 1v2a2 2 0 0 1-2 2A10 10 0 0 1 0 2a2 2 0 0 1 2-2z"/></svg><span>0861 204 375</span></div>
    <div class="contact-line"><svg viewBox="0 0 12 12"><path d="M0 2h12v8H0zm1 1 5 4 5-4" fill="none" stroke="#777" stroke-width="1.4"/></svg><span>hello@toncielbrode.com</span></div>
  </div>
  <div class="foot-col" style="left:657px">
    <h5>FOLLOW US ON</h5>
    <div class="socials"><span><i></i></span><span><i></i></span></div>
  </div>
  <div class="foot-col" style="left:851px;width:252px;height:220px">
    <h5>GET IN TOUCH</h5>
    <div class="field" style="left:0;top:33px;width:118px;height:23px">Name</div>
    <div class="field" style="left:130px;top:33px;width:122px;height:23px">Email</div>
    <div class="field" style="left:0;top:66px;width:252px;height:58px">Message</div>
    <a class="send" href="#">SEND</a>
  </div>
  <a class="to-top" href="#" aria-label="Back to top"><svg width="12" height="12" viewBox="0 0 12 12"><path d="M6 10V2M2 6l4-4 4 4" fill="none" stroke="#fff" stroke-width="1.8"/></svg></a>
  <div class="footer-rule"></div>
  <p class="copyright">© 2017, ton ciel brodé. All rights reserved</p>
</footer>

</body>
</html>
```